Innovative Consulting Firm Needs New Business Cards and Stationary

Our Innovative Consulting Firm, Larkfield Consulting, is in need of new business cards and stationary designs. We want two-sided cards that incorporate our logo, which is attached. We are looking for something not too formal, but is professional and slick.

Card should have the following information:
Name (ex. Tom Bradley)
Title (ex. Manager)
Address (ex. 24680 Cedar Lane)
Address 2 (ex. Suite 100)
City
State
Zip Code
Mobile
Email

The card should also have our website: www.larkfieldconsulting.example

Industry/Entity Type

Management Consulting

Contact Information for Business Card

Name (ex. Tom Bradley)
Title (ex. Manager)
Address 2 (ex. Suite 100)
City
State
Zip Code
Mobile
Email

Font styles to use
Sans Serif

Requirements
Must have
• The colors on the card must match the colors in the logo. The exact color codes are attached in a pdf.
Nice to have
• The Company's Tagline is "Focused on your Future". This might be nice to incorporate, but not necessary.

```html
<!DOCTYPE html>
<html lang="en">
<head>
<meta charset="utf-8">
<title>Larkfield Consulting – Business Card</title>
<link rel="stylesheet" href="https://fonts.googleapis.com/css2?family=Open+Sans:wdth,wght@75..100,300..700&display=swap">
<style>
  :root {
    --brand-yellow: #f2b31b;
    --brand-navy: #1d4f7c;
    --card-white: #ffffff;
    --backdrop: #3b3340;
    --card-shadow: rgba(0, 0, 0, 0.35);
  }
  * { box-sizing: border-box; margin: 0; padding: 0; }
  html, body {
    width: 1200px;
    height: 800px;
    overflow: hidden;
    background: var(--backdrop);
    font-family: "Open Sans", Arial, sans-serif;
  }
  .stage {
    width: 1200px;
    height: 800px;
    display: flex;
    align-items: center;
    justify-content: center;
    gap: 60px;
  }
  .card {
    position: relative;
    width: 525px;
    height: 300px;
    border-radius: 4px;
    box-shadow: 0 14px 30px var(--card-shadow);
    overflow: hidden;
  }

  /* Front side */
  .card--front {
    background: var(--brand-yellow);
    color: var(--card-white);
  }
  .card--front .wordmark {
    position: absolute;
    left: 0; right: 0;
    top: 110px;
    display: flex;
    align-items: center;
    justify-content: center;
    gap: 12px;
  }
  .wordmark__dot {
    width: 18px; height: 18px;
    border-radius: 50%;
    background: currentColor;
    flex: none;
  }
  .wordmark__name {
    font-size: 34px;
    font-weight: 600;
    letter-spacing: 0.5px;
    line-height: 1;
  }
  .tagline {
    position: absolute;
    left: 0; right: 0;
    bottom: 52px;
    text-align: center;
    font-size: 17px;
    font-weight: 400;
    font-stretch: 75%;
    text-transform: uppercase;
    letter-spacing: 0.5px;
  }

  /* Back side */
  .card--back {
    background: var(--card-white);
    color: var(--brand-navy);
  }
  .card--back .wordmark {
    position: absolute;
    left: 42px;
    top: 36px;
    display: flex;
    align-items: center;
    gap: 9px;
  }
  .card--back .wordmark__dot {
    width: 13px; height: 13px;
    background: var(--brand-yellow);
  }
  .card--back .wordmark__name {
    font-size: 23px;
    color: var(--brand-navy);
  }
  .holder {
    position: absolute;
    left: 42px;
    top: 150px;
  }
  .holder__name {
    font-size: 21px;
    font-weight: 400;
    font-stretch: 87%;
    text-transform: uppercase;
    line-height: 1.1;
  }
  .holder__title {
    font-size: 9px;
    font-stretch: 87%;
    text-transform: uppercase;
    margin-top: 2px;
  }
  .contacts {
    position: absolute;
    left: 265px;
    top: 112px;
    list-style: none;
    display: flex;
    flex-direction: column;
    gap: 12px;
  }
  .contact {
    display: flex;
    align-items: center;
    gap: 10px;
  }
  .contact__icon {
    width: 34px; height: 34px;
    flex: none;
  }
  .contact__text {
    font-size: 12.5px;
    line-height: 1.35;
  }
</style>
</head>
<body>
  <main class="stage">
    <section class="card card--front" aria-label="Business card front">
      <div class="wordmark">
        <span class="wordmark__dot"></span>
        <span class="wordmark__name">Larkfield Consulting</span>
      </div>
      <p class="tagline">Focused on your future</p>
    </section>

    <section class="card card--back" aria-label="Business card back">
      <div class="wordmark">
        <span class="wordmark__dot"></span>
        <span class="wordmark__name">Larkfield Consulting</span>
      </div>

      <div class="holder">
        <p class="holder__name">Tom Bradley</p>
        <p class="holder__title">Manager</p>
      </div>

      <ul class="contacts">
        <li class="contact">
          <svg class="contact__icon" viewBox="0 0 34 34" aria-hidden="true">
            <circle cx="17" cy="17" r="15.5" fill="none" stroke="var(--brand-yellow)" stroke-width="2"/>
            <path d="M17 8a6 6 0 0 0-6 6c0 4.5 6 11 6 11s6-6.5 6-11a6 6 0 0 0-6-6z" fill="var(--brand-yellow)"/>
            <circle cx="17" cy="14" r="2.2" fill="var(--card-white)"/>
          </svg>
          <p class="contact__text">24680 Cedar Lane, Suite 100<br>City, State, Zip Code</p>
        </li>
        <li class="contact">
          <svg class="contact__icon" viewBox="0 0 34 34" aria-hidden="true">
            <circle cx="17" cy="17" r="15.5" fill="none" stroke="var(--brand-yellow)" stroke-width="2"/>
            <path d="M13 9c1 0 2 2.5 2 3.5s-1.5 1.2-1.2 2.3c.5 1.8 2 3.6 3.4 4.6.8.5 1.4-.9 2.3-.9s3.5 1.2 3.5 2.1c0 1.3-1.6 3.4-3.5 3-4.8-1-9.5-7-9.5-11.4C10 10.6 11.8 9 13 9z" fill="var(--brand-yellow)"/>
          </svg>
          <p class="contact__text">09125550148</p>
        </li>
        <li class="contact">
          <svg class="contact__icon" viewBox="0 0 34 34" aria-hidden="true">
            <circle cx="17" cy="17" r="15.5" fill="none" stroke="var(--brand-yellow)" stroke-width="2"/>
            <circle cx="11.5" cy="22.5" r="2" fill="var(--brand-yellow)"/>
            <path d="M10 16.5a7.5 7.5 0 0 1 7.5 7.5M10 12a12 12 0 0 1 12 12" fill="none" stroke="var(--brand-yellow)" stroke-width="2.2" stroke-linecap="round"/>
          </svg>
          <p class="contact__text">info@larkfieldconsulting.example<br>www.larkfieldconsulting.example</p>
        </li>
      </ul>
    </section>
  </main>
</body>
</html>
```